Technology Charity needs a Web Design

Vendra Lum purchases used company mobiles and donates the proceeds to charity. It is showing companies how they can do social good, with unused technology. We would like to see designs with relevant images of social good. Open to ideas, and more is explained in the attached brief. Logo is attached as well.

```html
<!DOCTYPE html>
<html lang="en">
<head>
<meta charset="utf-8">
<title>Vendra Lum — Tech for social good</title>
<link href="https://fonts.googleapis.com/css2?family=Montserrat:wght@400;500;600;700;800&family=Open+Sans:wght@400;600&display=swap" rel="stylesheet">
<style>
:root{
  --olive:#b7bc98;
  --blue:#7b9faa;
  --ink:#1f1f1f;
  --text:#333;
  --line:#b9b9b9;
  --soft:#f3f0f0;
  --white:#fff;
  --faint:#efefef;
}
*{box-sizing:border-box;margin:0;padding:0}
html,body{width:1200px;height:3752px;overflow:hidden}
body{position:relative;background:var(--white);font-family:"Open Sans",Arial,sans-serif;color:var(--text)}
.abs{position:absolute}
.heading{font-family:"Montserrat",Arial,sans-serif;font-weight:700;color:var(--ink);font-size:22px;letter-spacing:.3px}
.btn{position:absolute;background:var(--olive);color:var(--white);font-family:"Montserrat",Arial,sans-serif;font-weight:700;font-size:11px;letter-spacing:.6px;display:flex;align-items:center;justify-content:center}

/* header */
.site-header{position:absolute;left:0;top:0;width:1200px;height:102px;background:var(--white)}
.brand{position:absolute;left:130px;top:26px;display:flex;align-items:center;gap:12px}
.brand-mark{width:26px;height:26px;background:var(--olive)}
.brand-name{font-family:"Montserrat",Arial,sans-serif;font-weight:600;font-size:32px;color:var(--blue)}
.donate{left:752px;top:18px;width:102px;height:33px;font-size:14px}
.mail-icon{left:872px;top:28px}
.mail-divider{left:908px;top:20px;width:2px;height:32px;background:var(--ink)}
.mail-label{left:925px;top:22px;font-size:11px;font-family:"Montserrat",Arial,sans-serif;font-weight:500;color:var(--ink)}
.mail-address{left:925px;top:37px;font-size:15px;color:var(--ink)}
.main-nav{position:absolute;top:73px;left:0;font-family:"Montserrat",Arial,sans-serif;font-weight:600;font-size:12px;color:var(--ink)}
.main-nav span{position:absolute;white-space:nowrap}
.main-nav .active{color:var(--blue)}

/* hero */
.hero{position:absolute;left:0;top:102px;width:1200px;height:556px;overflow:hidden}
.hero-photo{position:absolute;inset:0;background:linear-gradient(100deg,#2f4a4c 0%,#435a5a 25%,#6b6357 45%,#2b2a27 70%,#1a1a1a 100%)}
.hero-title{left:766px;top:318px;font-family:"Montserrat",Arial,sans-serif;font-weight:800;font-size:41px;line-height:42px;color:#2b2b2b}
.hero-more{left:997px;top:440px;width:110px;height:35px;background:var(--white);color:var(--olive);font-size:14px}
.hero-dots{left:556px;top:511px;display:flex;gap:13px}
.hero-dots i{width:8px;height:8px;border-radius:50%;background:var(--white);display:block}
.hero-dots i.off{background:transparent;border:1.5px solid var(--white)}

/* benefits */
.section-rule{position:absolute;width:30px;height:4px;background:var(--olive)}
.benefit{position:absolute;width:255px;height:272px;border:2px solid var(--line);outline:1px solid var(--line);outline-offset:-6px;text-align:center;padding:0 26px}
.benefit svg{position:absolute;left:102px;top:34px}
.benefit h3{position:absolute;left:14px;right:14px;top:114px;font-family:"Montserrat",Arial,sans-serif;font-weight:500;font-size:14.5px;line-height:18px;color:var(--ink)}
.benefit p{position:absolute;left:24px;right:24px;top:164px;font-size:11px;line-height:15px;color:var(--text)}
.benefit .btn{left:84px;top:224px;width:86px;height:22px;font-size:10px}

/* mission */
.mission-heading{left:738px;top:1522px}
.mission-text{left:738px;top:1590px;width:310px;font-size:16px;line-height:20.8px;color:var(--ink)}
.mission-more{left:742px;top:1814px;width:110px;height:34px;font-size:12px}

/* how it works */
.step{position:absolute;width:245px;height:284px;background:var(--white);box-shadow:0 2px 10px rgba(0,0,0,.12);text-align:center}
.step svg{position:absolute;left:97px;top:40px}
.step p{position:absolute;left:36px;right:36px;top:110px;font-size:11.5px;line-height:16.6px;color:var(--ink)}
.step .num{position:absolute;left:10px;bottom:-6px;font-family:"Montserrat",Arial,sans-serif;font-weight:800;font-size:56px;color:var(--faint)}

/* what we do */
.what-we-do{position:absolute;left:0;top:2861px;width:1200px;height:495px;background:var(--soft);overflow:hidden}
.wwd-heading{left:146px;top:2978px}
.wwd-text{left:146px;top:3036px;width:392px;font-size:16px;line-height:20.8px;color:var(--ink)}
.wwd-more{left:150px;top:3222px;width:109px;height:34px;font-size:12px}

/* footer */
.site-footer{position:absolute;left:0;top:3356px;width:1200px;height:396px;background:var(--blue);color:var(--white);overflow:hidden}
.footer-title{position:absolute;font-family:"Montserrat",Arial,sans-serif;font-weight:700;font-size:14px;letter-spacing:.4px}
.footer-menu span{position:absolute;left:498px;font-size:14px;letter-spacing:.4px}
.field{position:absolute;left:702px;width:189px;background:var(--white);color:#555;font-size:9.5px;padding:5px 9px;font-family:"Montserrat",Arial,sans-serif}
.submit{left:702px;top:221px;width:189px;height:32px;font-size:13px}
.social{position:absolute;left:948px;display:flex;align-items:center;gap:14px;font-size:14px;line-height:18px}
.social i{width:28px;height:28px;border-radius:50%;background:var(--white);display:block}
.footer-divider{position:absolute;left:131px;top:310px;width:942px;height:1px;background:rgba(255,255,255,.35)}
.copyright{position:absolute;left:0;width:1200px;top:354px;text-align:center;font-size:11px}
</style>
</head>
<body>

<header class="site-header">
  <div class="brand"><span class="brand-mark"></span><span class="brand-name">Vendra Lum</span></div>
  <div class="btn donate">DONATE</div>
  <svg class="abs mail-icon" width="24" height="17" viewBox="0 0 24 17"><rect x="1" y="1" width="22" height="15" fill="none" stroke="#555" stroke-width="1.4"/><path d="M1 1l11 9 11-9M1 16l8-7M23 16l-8-7" fill="none" stroke="#555" stroke-width="1.4"/></svg>
  <div class="abs mail-divider"></div>
  <div class="abs mail-label">E MAIL US</div>
  <div class="abs mail-address">hello@vendralum.org</div>
  <nav class="main-nav">
    <span class="active" style="left:533px">WHAT WE DO</span>
    <span style="left:641px">BENEFITS</span>
    <span style="left:728px">HOW DOES IT WORK?</span>
    <span style="left:885px">CONTACT US</span>
    <span style="left:986px">OUR MISSION</span>
  </nav>
</header>

<section class="hero">
  <div class="hero-photo" role="img" aria-label="Photo of a smiling young man holding a tablet beside a glass whiteboard in a bright office"></div>
  <svg class="abs" style="left:0;top:0" width="1200" height="556">
    <circle cx="1090" cy="330" r="270" fill="var(--blue)"/>
    <circle cx="880" cy="390" r="220" fill="var(--olive)"/>
  </svg>
  <div class="abs hero-title">TECH<br>FOR SOCIAL<br>GOOD</div>
  <div class="btn hero-more">READ MORE</div>
  <div class="abs hero-dots"><i></i><i></i><i class="off"></i><i></i><i></i></div>
</section>

<!-- benefits -->
<div class="section-rule" style="left:585px;top:704px"></div>
<h2 class="abs heading" style="left:0;width:1200px;text-align:center;top:737px">BENEFITS</h2>

<div class="benefit" style="left:192px;top:798px">
  <svg width="50" height="52" viewBox="0 0 50 52"><circle cx="25" cy="20" r="15" fill="none" stroke="var(--blue)" stroke-width="3"/><circle cx="25" cy="20" r="6" fill="var(--blue)"/><path d="M15 31l-6 16 8-3 4 7 4-14M35 31l6 16-8-3-4 7-4-14" fill="none" stroke="var(--blue)" stroke-width="3"/></svg>
  <h3>Improve Organisational Reputation</h3>
  <p>Individuals and communities have great respect for organisations that take initiatives for social good.</p>
  <div class="btn">READ MORE</div>
</div>
<div class="benefit" style="left:472px;top:798px">
  <svg width="50" height="52" viewBox="0 0 50 52"><rect x="8" y="2" width="24" height="46" rx="3" fill="none" stroke="var(--blue)" stroke-width="3"/><circle cx="33" cy="22" r="11" fill="var(--white)" stroke="var(--blue)" stroke-width="2.5"/><text x="33" y="27" text-anchor="middle" font-size="14" font-family="Montserrat" font-weight="700" fill="var(--blue)">$</text></svg>
  <h3>Provide a simple and effective channel for re-use.</h3>
  <p>We make it easier to clear outdated stock, paving the way for new technology as well as a tax</p>
  <div class="btn">READ MORE</div>
</div>
<div class="benefit" style="left:751px;top:798px">
  <svg width="54" height="52" viewBox="0 0 54 52"><circle cx="28" cy="25" r="22" fill="none" stroke="var(--blue)" stroke-width="3"/><path d="M6 25h44M28 3c-9 10-9 34 0 44M28 3c9 10 9 34 0 44" fill="none" stroke="var(--blue)" stroke-width="2"/><path d="M16 40c-8-8-6-18 4-20 2 8-1 15-4 20z" fill="var(--blue)"/></svg>
  <h3 style="top:118px">Environmentally friendly</h3>
  <p>By repurposing used mobiles, for reuse or recycling, extends the life, therefore benefiting</p>
  <div class="btn">READ MORE</div>
</div>
<div class="benefit" style="left:192px;top:1089px">
  <svg width="56" height="52" viewBox="0 0 56 52"><rect x="24" y="2" width="28" height="24" rx="3" fill="var(--blue)"/><text x="38" y="21" text-anchor="middle" font-size="17" font-family="Montserrat" font-weight="700" fill="var(--white)">%</text><circle cx="12" cy="42" r="6" fill="none" stroke="var(--blue)" stroke-width="3"/><circle cx="26" cy="42" r="6" fill="none" stroke="var(--blue)" stroke-width="3"/><path d="M15 37l14-26M23 37l-10-22" stroke="var(--blue)" stroke-width="3"/></svg>
  <h3>Offer benefits for your brand</h3>
  <p>Customers are willing to pay premium rates for goods from a sustainable and responsible</p>
  <div class="btn">READ MORE</div>
</div>
<div class="benefit" style="left:472px;top:1089px">
  <svg width="50" height="56" viewBox="0 0 50 56"><path d="M25 2c9 8 11 20 9 32H16c-2-12 0-24 9-32z" fill="none" stroke="var(--blue)" stroke-width="3"/><circle cx="25" cy="20" r="4" fill="var(--blue)"/><path d="M16 28l-8 9 8 0M34 28l8 9-8 0" fill="var(--blue)"/><path d="M20 40l5 12 5-12z" fill="var(--blue)"/></svg>
  <h3>Boost company morale</h3>
  <p>People are happier when working at socially responsible companies– your staff might even surprise you with</p>
  <div class="btn">READ MORE</div>
</div>
<div class="benefit" style="left:751px;top:1089px">
  <svg width="54" height="54" viewBox="0 0 54 54"><path d="M16 2h26l8 8v42H16z" fill="none" stroke="var(--blue)" stroke-width="3"/><path d="M28 44V32M35 44V26M42 44V20" stroke="var(--blue)" stroke-width="3"/><circle cx="14" cy="30" r="12" fill="var(--blue)"/><text x="14" y="36" text-anchor="middle" font-size="16" font-family="Montserrat" font-weight="700" fill="var(--white)">$</text></svg>
  <h3 style="top:118px">Entice millenials</h3>
  <p>They account for the largest perecentage of the global workforce and drive trillions of dollars in</p>
  <div class="btn">READ MORE</div>
</div>

<!-- mission -->
<svg class="abs" style="left:0;top:1456px" width="740" height="500">
  <circle cx="470" cy="270" r="225" fill="var(--blue)"/>
  <circle cx="220" cy="230" r="220" fill="var(--olive)"/>
</svg>
<h2 class="abs heading mission-heading">OUR MISSION</h2>
<div class="section-rule" style="left:740px;top:1556px;width:48px;height:2px"></div>
<p class="abs mission-text">There are thousands of mobiles lying around in offices around Australia. The IT department tend to be at a loss of what to do with them. Most just get taken by the eco-waste collections. Vendra Lum offers a solution to pay for the recycle and give the proceeds to Social Good. Now that back room full of used technology, is your company’s pathway to social good.</p>
<div class="btn mission-more">READ MORE</div>

<!-- how it works -->
<div class="section-rule" style="left:585px;top:2044px"></div>
<h2 class="abs heading" style="left:0;width:1200px;text-align:center;top:2084px">HOW DOES IT WORK?</h2>

<svg class="abs" style="left:0;top:2150px" width="1200" height="760">
  <g fill="none" stroke="#777" stroke-width="1.4" stroke-dasharray="2 3">
    <path d="M182 146H130V475H182"/>
    <path d="M427 146H478M722 146H773"/>
    <path d="M1018 146H1073V475H1018"/>
    <path d="M427 475H478M722 475H773"/>
  </g>
  <polygon points="130,160 114,188 146,188" fill="var(--olive)"/>
  <polygon points="1073,398 1050,434 1096,434" fill="var(--blue)"/>
  <g fill="none" stroke="#555" stroke-width="1.4">
    <path d="M453 141l5 5-5 5M459 141l5 5-5 5M748 141l5 5-5 5M754 141l5 5-5 5"/>
    <path d="M457 470l-5 5 5 5M451 470l-5 5 5 5M752 470l-5 5 5 5M746 470l-5 5 5 5"/>
  </g>
  <polygon points="1037,686 1080,710 1037,734" fill="var(--blue)"/>
</svg>

<div class="step" style="left:182px;top:2162px">
  <svg width="50" height="50" viewBox="0 0 50 50"><path d="M8 6l8-2 6 11-5 4c3 6 8 11 14 14l4-5 11 6-2 8c-18 0-36-18-36-36z" fill="var(--blue)"/><path d="M30 6a14 14 0 0 1 14 14M30 12a8 8 0 0 1 8 8" fill="none" stroke="var(--blue)" stroke-width="2.5"/></svg>
  <p>Contact Vendra Lum directly by calling xxx, or by completing your details on our form (Click here) and we will contact you.</p>
  <span class="num">1</span>
</div>
<div class="step" style="left:478px;top:2162px">
  <svg width="60" height="50" viewBox="0 0 60 50" style="left:92px"><circle cx="14" cy="10" r="6" fill="var(--blue)"/><circle cx="46" cy="10" r="6" fill="var(--blue)"/><path d="M6 20h14v14H6zM40 20h14v14H40zM14 24h32v5H14zM26 29h8v16h-8zM6 34v12M54 34v12" fill="var(--blue)" stroke="var(--blue)" stroke-width="2"/></svg>
  <p>Vendra Lum employee can either visit your office to review the stock, or you can send a listing of the mobile model numbers. Alternative arrangements can be made to review your stock. Whatever is the easiest and convenient to you.</p>
  <span class="num">2</span>
</div>
<div class="step" style="left:773px;top:2162px">
  <svg width="50" height="50" viewBox="0 0 50 50"><rect x="16" y="2" width="30" height="44" rx="3" fill="none" stroke="var(--blue)" stroke-width="3"/><rect x="21" y="7" width="20" height="8" fill="var(--blue)"/><path d="M22 21h4v4h-4zM30 21h4v4h-4zM38 21h3v4h-3zM30 29h4v4h-4zM38 29h3v4h-3zM30 37h4v4h-4zM38 37h3v4h-3z" fill="var(--blue)"/><circle cx="14" cy="36" r="11" fill="var(--blue)"/><text x="14" y="41" text-anchor="middle" font-size="14" font-family="Montserrat" font-weight="700" fill="var(--white)">$</text></svg>
  <p>Vendra Lum provides you with an estimated valuation, with a listing of the stock.</p>
  <span class="num">3</span>
</div>
<div class="step" style="left:182px;top:2482px">
  <svg width="50" height="50" viewBox="0 0 50 50"><path d="M8 2h24l8 8v36H8z" fill="none" stroke="var(--blue)" stroke-width="3"/><path d="M14 16h18M14 22h18M14 28h12" stroke="var(--blue)" stroke-width="2.5"/><circle cx="38" cy="38" r="10" fill="var(--white)" stroke="var(--blue)" stroke-width="3"/><path d="M34 42l7-7" stroke="var(--blue)" stroke-width="3"/></svg>
  <p>Once this is agreed upon, you nominate the charity you would like the money to go towards, or alternatively we pay you directly. This is all agreed in writing.</p>
  <span class="num">4</span>
</div>
<div class="step" style="left:478px;top:2482px">
  <svg width="60" height="50" viewBox="0 0 60 50" style="left:92px"><rect x="2" y="8" width="54" height="34" rx="3" fill="var(--blue)"/><rect x="2" y="16" width="54" height="7" fill="var(--white)"/><path d="M8 32h18" stroke="var(--white)" stroke-width="3"/><circle cx="46" cy="38" r="9" fill="var(--white)"/><path d="M41 38l4 4 7-8" fill="none" stroke="var(--blue)" stroke-width="3"/></svg>
  <p>Payment is made to nominated charity by Vendra Lum, on behalf of you. This is stated to the charity. Alternatively, we pay you directly for the stock.</p>
  <span class="num">5</span>
</div>
<div class="step" style="left:773px;top:2482px">
  <svg width="70" height="50" viewBox="0 0 70 50" style="left:87px"><rect x="6" y="14" width="26" height="26" fill="var(--olive)"/><circle cx="48" cy="27" r="16" fill="var(--blue)"/></svg>
  <p>Vendra Lum arranges pick-up of the stock. NB: Our employees are young people, mainly students. One of our missions is to teach our young people vital future skills, including business etiquette and dealings.</p>
  <span class="num">6</span>
</div>

<!-- what we do -->
<section class="what-we-do">
  <svg class="abs" style="left:0;top:0" width="1200" height="495">
    <polygon points="55,342 -60,495 150,495" fill="#dedbdb"/>
    <defs><clipPath id="photoFrame"><polygon points="833,0 546,495 1121,495"/></clipPath></defs>
    <rect x="540" y="0" width="590" height="495" fill="url(#photoTone)" clip-path="url(#photoFrame)" role="img" aria-label="Photo of a smiling young woman in glasses seated at a laptop"/>
    <linearGradient id="photoTone" x1="0" y1="0" x2="1" y2="1"><stop offset="0" stop-color="#2a2622"/><stop offset=".55" stop-color="#6b6a64"/><stop offset="1" stop-color="#b57a2e"/></linearGradient>
  </svg>
</section>
<div class="section-rule" style="left:148px;top:2944px"></div>
<h2 class="abs heading wwd-heading">WHAT WE DO</h2>
<p class="abs wwd-text">Vendra Lum creates an easy pathway for organisations, to become more sustainable, renewable and give back to the community. We do this by purchasing used employee mobiles, and donating the proceeds to social good, on behalf of organisations. Helping organisation give to meaningful causes that do so much for the community.</p>
<div class="btn wwd-more">READ MORE</div>

<!-- footer -->
<footer class="site-footer">
  <svg class="abs" style="left:120px;top:40px" width="340" height="240">
    <circle cx="215" cy="125" r="100" fill="var(--white)"/>
    <circle cx="110" cy="110" r="95" fill="var(--olive)"/>
  </svg>
  <div class="footer-title" style="left:498px;top:55px">MENU</div>
  <div class="footer-menu">
    <span style="top:100px">WHAT WE DO</span>
    <span style="top:124px">BENEFITS</span>
    <span style="top:148px">HOW DOES IT WORK?</span>
    <span style="top:172px">CONTACT US</span>
    <span style="top:196px">OUR MISSION</span>
  </div>
  <div class="footer-title" style="left:702px;top:55px">CONTACT US</div>
  <div class="field" style="top:93px;height:23px">NAME</div>
  <div class="field" style="top:125px;height:23px">E MAIL</div>
  <div class="field" style="top:156px;height:55px">MESSAGE</div>
  <div class="btn submit">SUBMIT</div>
  <div class="footer-title" style="left:951px;top:55px">FOLLOW US</div>
  <div class="social" style="top:99px"><i></i><span>Like us on<br>FRIENDWALL</span></div>
  <div class="social" style="top:161px"><i></i><span>Follow us on<br>CHIRPER</span></div>
  <div class="social" style="top:222px"><i></i><span>Follow us on<br>WORKMESH</span></div>
  <div class="footer-divider"></div>
  <div class="copyright">Copyright © 2020 All Rights Reserved</div>
</footer>

</body>
</html>
```